Design a business card for Harbor Profile

I need a business card designed for a new company called HarborProfile.example . I will be doing a lot of networking and the business card is the first thing people will see. I need to get them to my website. I already have a logo and attached it here.
A Harbor Profile is a personal website with career tools to promote your professional success. For more information, visit HarborProfile.example .

My tag line is Stride Out-and Prevail although if there is room, I would rather use - Don't leave your career up to someone else. Stride Out-and Prevail.

My target customer is the professional who is successful at their job but needs to get to the next level in their career. Essentially, everyone on Workmesh.example that does not own their own company.

Other information for the card:

Ned Varcoe
CEO

555-014-7732

Ned@HarborProfile.example

HarborProfile.example

I need a high resolution deign ready to print. I also need the original PSD files.

Target Market(s)

Professionals in the growth phase of their career

Industry/Entity Type

Business

Contact Information for Business Card

Don't leave your career up to someone else. Stride Out-and Prevail.

Ned Varcoe
CEO

555-014-7732

Ned@HarborProfile.example

HarborProfile.example

Font styles to use
Serif

Requirements
Must have
• My log and original colors, Images and it has to be fun and very impressive

```html
<!DOCTYPE html>
<html lang="en">
<head>
<meta charset="utf-8">
<title>Harbor Profile — Business Card</title>
<link rel="stylesheet" href="https://fonts.googleapis.com/css2?family=Libre+Baskerville:ital,wght@0,400;0,700;1,400&display=swap">
<style>
  :root {
    --maroon: #7a2b47;
    --slate: #3d4853;
    --paper: #ffffff;
    --paper-shade: #e9e9ea;
    --silver-light: #f4f4f4;
    --silver-dark: #a9abae;
    --stage: #ebe7e2;
    --ink-light: #f2f2f2;
  }
  * { box-sizing: border-box; margin: 0; padding: 0; }
  html, body {
    width: 1200px;
    height: 828px;
    overflow: hidden;
    background: var(--stage);
    font-family: "Libre Baskerville", Georgia, serif;
  }
  .canvas {
    position: relative;
    width: 1200px;
    height: 828px;
  }
  .card {
    position: absolute;
    top: 260px;
    width: 540px;
    height: 309px;
    overflow: hidden;
    background: var(--paper);
    box-shadow: 0 6px 18px rgba(0,0,0,0.18);
  }
  .card--front { left: 40px; }
  .card--back { left: 620px; }
  .card__art {
    position: absolute;
    inset: 0;
    width: 100%;
    height: 100%;
  }
  .brand {
    position: absolute;
    display: flex;
    align-items: center;
    gap: 8px;
  }
  .brand__dot {
    width: 22px;
    height: 22px;
    border-radius: 50%;
    background: var(--maroon);
  }
  .brand__name {
    font-weight: 700;
    font-size: 24px;
    letter-spacing: 1px;
    text-transform: uppercase;
    color: var(--slate);
    line-height: 1;
  }
  .card--front .brand { left: 46px; top: 118px; }
  .card--back .brand { left: 30px; top: 218px; }
  .card--back .brand__name { font-size: 19px; }
  .card--back .brand__dot { width: 16px; height: 16px; }

  .front__url {
    position: absolute;
    right: 40px;
    bottom: 34px;
    color: var(--ink-light);
    font-size: 13px;
    letter-spacing: 3px;
  }

  .details {
    position: absolute;
    right: 26px;
    top: 24px;
    width: 300px;
    text-align: right;
    color: var(--ink-light);
  }
  .details__name {
    font-size: 18px;
    font-weight: 400;
    letter-spacing: 2px;
    text-transform: uppercase;
  }
  .details__role {
    font-size: 11px;
    margin-top: 4px;
    letter-spacing: 0.5px;
  }
  .details__tagline {
    margin-top: 24px;
    font-size: 10.5px;
    font-style: italic;
    line-height: 1.6;
  }
  .contact-list {
    list-style: none;
    margin-top: 20px;
    font-size: 10.5px;
    letter-spacing: 0.3px;
  }
  .contact-list li {
    display: flex;
    justify-content: flex-end;
    align-items: center;
    gap: 7px;
    height: 19px;
  }
  .contact-list svg {
    width: 11px;
    height: 11px;
    fill: none;
    stroke: var(--ink-light);
    stroke-width: 1.4;
  }
</style>
</head>
<body>
<main class="canvas">

  <section class="card card--front" aria-label="Business card front">
    <svg class="card__art" viewBox="0 0 540 309" preserveAspectRatio="none" aria-hidden="true">
      <defs>
        <linearGradient id="paperFade" x1="0" y1="0" x2="0" y2="1">
          <stop offset="0" stop-color="#ffffff"/>
          <stop offset="1" stop-color="#e9e9ea"/>
        </linearGradient>
        <linearGradient id="silverEdge" x1="0" y1="0" x2="1" y2="0">
          <stop offset="0" stop-color="#a9abae"/>
          <stop offset="0.55" stop-color="#f4f4f4"/>
          <stop offset="1" stop-color="#a9abae"/>
        </linearGradient>
      </defs>
      <rect width="540" height="309" fill="url(#paperFade)"/>
      <path d="M0 198 Q320 196 540 26 L540 50 Q320 214 0 216 Z" fill="url(#silverEdge)"/>
      <path d="M0 214 Q320 212 540 46 L540 309 L0 309 Z" fill="#7a2b47"/>
    </svg>
    <div class="brand">
      <span class="brand__dot"></span>
      <span class="brand__name">Harbor Profile</span>
    </div>
    <p class="front__url">www.harborprofile.example</p>
  </section>

  <section class="card card--back" aria-label="Business card back">
    <svg class="card__art" viewBox="0 0 540 309" preserveAspectRatio="none" aria-hidden="true">
      <rect width="540" height="309" fill="#ffffff"/>
      <path d="M0 0 L540 0 L540 309 L380 309 C350 205 230 140 0 160 Z" fill="#7a2b47"/>
      <path d="M0 0 L540 0 L540 309 L396 309 C366 195 240 128 0 146 Z" fill="#3d4853"/>
    </svg>
    <div class="brand">
      <span class="brand__dot"></span>
      <span class="brand__name">Harbor Profile</span>
    </div>
    <div class="details">
      <h1 class="details__name">Ned Varcoe</h1>
      <p class="details__role">CEO</p>
      <p class="details__tagline">Don't leave your career up to someone else.<br>Stride Out-and Prevail.</p>
      <ul class="contact-list">
        <li>555-014-7732
          <svg viewBox="0 0 12 12"><path d="M2 1.5 L4.2 1.5 L5 4 L3.8 5 Q5 7.4 7 8.2 L8 7 L10.5 7.8 L10.5 10 Q5 11 1.5 3.5 Z"/></svg>
        </li>
        <li>Ned@HarborProfile.example
          <svg viewBox="0 0 12 12"><rect x="1" y="2.5" width="10" height="7"/><path d="M1 2.5 L6 6.5 L11 2.5"/></svg>
        </li>
        <li>HarborProfile.example
          <svg viewBox="0 0 12 12"><circle cx="6" cy="6" r="4.8"/><ellipse cx="6" cy="6" rx="2" ry="4.8"/><path d="M1.2 6 H10.8"/></svg>
        </li>
      </ul>
    </div>
  </section>

</main>
</body>
</html>
```